Powerpoint template

I am looking for a brand based PPT template that can also be used as the basis for datasheet creation. I have attached a document with some of our branding structure in as an FYI to help.

To be clear I am looking a background design, bullets, layouts, different styles for differing content types. This is a template to be used for lots of presentations.
Updates

Project Deadline Extended
Reason: I have committed to the payment and wanted to give people chance to respond.

Target Market(s)

Enterprise

Requirements
Must have
• Brand standard. different page design choices for different content types
Nice to have
• brand font if it works. Use of some play on the logo in bullets
Should not have
• must be on brand and focused on the business audience

```html
<!DOCTYPE html>
<html lang="en">
<head>
<meta charset="utf-8">
<title>Lumenware Presentation Template</title>
<link rel="stylesheet" href="https://fonts.googleapis.com/css2?family=Ubuntu:wght@400;500&display=swap">
<style>
  :root {
    --frame: #4a5258;
    --brand-blue: #00a3d9;
    --brand-blue-deep: #2a8bcb;
    --brand-green: #8cc63f;
    --brand-navy: #2a3445;
    --brand-mist: #eef1f5;
    --white: #ffffff;
    --sub-green: #9bc83c;
    --sub-blue: #1a8fd6;
  }
  * { box-sizing: border-box; margin: 0; padding: 0; }
  html, body {
    width: 1064px; height: 1200px; overflow: hidden;
    background: var(--frame);
    font-family: "Ubuntu", sans-serif;
  }
  .sheet { position: relative; width: 1064px; height: 1200px; }
  .slide {
    position: absolute; width: 516px; height: 387px; overflow: hidden;
  }
  .col-a { left: 12px; }
  .col-b { left: 537px; }
  .row-1 { top: 9px; }
  .row-2 { top: 407px; }
  .row-3 { top: 805px; }
  .slide--blue  { background: var(--brand-blue); }
  .slide--green { background: var(--brand-green); }
  .slide--navy  { background: var(--brand-navy); }
  .slide--mist  { background: var(--brand-mist); }
  .slide-texture {
    position: absolute; inset: 0;
    background: radial-gradient(ellipse 45% 70% at 80% 45%, rgba(0,0,0,0.05), rgba(0,0,0,0) 70%);
  }
  .slide--mist .slide-texture {
    background: radial-gradient(ellipse 45% 70% at 80% 45%, rgba(40,60,90,0.04), rgba(0,0,0,0) 70%);
  }
  .brand-dot {
    position: absolute; left: 70px; top: 158px;
    width: 66px; height: 66px; border-radius: 50%;
    background: var(--white);
  }
  .slide--navy .brand-dot, .slide--mist .brand-dot { background: var(--brand-green); }
  .brand-name {
    position: absolute; left: 158px; top: 170px;
    font-size: 60px; font-weight: 400; line-height: 1;
    letter-spacing: -1px; color: var(--white);
  }
  .slide--navy .brand-name, .slide--mist .brand-name { color: var(--brand-blue-deep); }
  .heading-dot { top: 160px; }
  .heading-block { position: absolute; left: 160px; top: 160px; }
  .heading-title {
    font-size: 41px; font-weight: 400; line-height: 1; color: var(--white);
  }
  .heading-sub {
    font-size: 18px; font-weight: 400; line-height: 1; margin-top: 5px;
  }
  .slide--blue .heading-sub { color: var(--sub-green); }
  .slide--green .heading-sub { color: var(--sub-blue); }
  .page-number {
    position: absolute; right: 14px; bottom: 9px;
    font-size: 8px; color: var(--white);
  }
</style>
</head>
<body>
<main class="sheet">
  <section class="slide slide--blue col-a row-1">
    <div class="slide-texture" role="img" aria-label="Faint flowchart pattern with large brand shape"></div>
    <span class="brand-dot"></span>
    <p class="brand-name">lumenware</p>
  </section>

  <section class="slide slide--green col-b row-1">
    <div class="slide-texture" role="img" aria-label="Faint flowchart pattern with large brand shape"></div>
    <span class="brand-dot"></span>
    <p class="brand-name">lumenware</p>
  </section>

  <section class="slide slide--navy col-a row-2">
    <div class="slide-texture" role="img" aria-label="Faint flowchart pattern with large brand shape"></div>
    <span class="brand-dot"></span>
    <p class="brand-name">lumenware</p>
  </section>

  <section class="slide slide--mist col-b row-2">
    <div class="slide-texture" role="img" aria-label="Faint flowchart pattern with large brand shape"></div>
    <span class="brand-dot"></span>
    <p class="brand-name">lumenware</p>
  </section>

  <section class="slide slide--blue col-a row-3">
    <div class="slide-texture" role="img" aria-label="Faint flowchart pattern background"></div>
    <span class="brand-dot heading-dot"></span>
    <div class="heading-block">
      <h1 class="heading-title">New Heading</h1>
      <p class="heading-sub">New Heading Subtitle</p>
    </div>
    <span class="page-number">5</span>
  </section>

  <section class="slide slide--green col-b row-3">
    <div class="slide-texture" role="img" aria-label="Faint flowchart pattern background"></div>
    <span class="brand-dot heading-dot"></span>
    <div class="heading-block">
      <h1 class="heading-title">New Heading</h1>
      <p class="heading-sub">New Heading Subtitle</p>
    </div>
    <span class="page-number">6</span>
  </section>
</main>
</body>
</html>
```